Brochure for concert

I need a brochure design for the concert. Attached please find last year's brochure (Oveli Concert Programme.pdf).
The contents of this year's brochure can be found in the document 'Concert program.docx.'
The design of the brochure should be consistent with the invitation card.

```html
<!DOCTYPE html>
<html lang="en">
<head>
<meta charset="utf-8">
<title>Band Foxglove Debut Concert Programme</title>
<link href="https://fonts.googleapis.com/css2?family=Cinzel:wght@400;500&family=Great+Vibes&family=Montserrat:wght@400;500;600&display=swap" rel="stylesheet">
<style>
:root{
  --paper:#ffffff;
  --teal-deep:#041517;
  --teal-mid:#0b3a3b;
  --teal-glow:#125553;
  --gold:#c9924a;
  --gold-light:#e8c27a;
  --ink:#f3ede2;
  --ink-soft:#d9d3c6;
}
*{margin:0;padding:0;box-sizing:border-box}
html,body{width:1200px;height:4117px;overflow:hidden;background:var(--paper)}
body{position:relative;font-family:'Montserrat',sans-serif;color:var(--ink)}
.page{
  position:absolute;width:475px;height:723px;overflow:hidden;
  background:radial-gradient(ellipse 80% 70% at 50% 75%,var(--teal-glow) 0%,var(--teal-mid) 40%,var(--teal-deep) 100%);
  box-shadow:0 4px 10px rgba(0,0,0,.35);
}
.frame{position:absolute;inset:22px;border:1px solid var(--gold);opacity:.75}
.frame::after{content:"";position:absolute;inset:4px;border:1px solid var(--gold);opacity:.5}
.lotus{position:absolute;border-radius:50%;
  background:radial-gradient(circle at 50% 50%,#1d6a66 0%,#0f4a48 45%,rgba(8,40,40,0) 72%)}
.lotus-left{left:-70px;bottom:-60px;width:230px;height:210px}
.lotus-right{right:-70px;bottom:-40px;width:220px;height:220px}
.lotus-mid{left:140px;bottom:-110px;width:200px;height:170px;opacity:.7}
.content{position:absolute;left:40px;right:40px;top:72px;text-align:center}
.title{font-family:'Cinzel',serif;font-weight:400;font-size:21px;letter-spacing:1px;color:var(--gold)}
.flourish{display:block;margin:2px auto 8px}
.intro{font-size:6.6px;line-height:1.6;color:var(--ink-soft);margin:0 8px 16px}
.lyrics{font-size:7.4px;line-height:1.75;color:var(--gold-light)}
.lyrics p{margin-bottom:10px}
.icon{display:block;margin:14px auto 0}

/* programme list */
.programme .section{margin-bottom:36px}
.programme .title{font-size:20px;margin-bottom:0}
.programme ul{list-style:none;font-size:9.5px;line-height:1.6;color:var(--ink)}

/* cover */
.cover .band-name{position:absolute;left:52px;top:58px;font-family:'Great Vibes',cursive;font-size:56px;color:var(--gold);line-height:1}
.cover .debut{position:absolute;left:60px;top:122px;font-size:19px;letter-spacing:1px;color:var(--gold-light)}
.cover .featuring{position:absolute;left:60px;top:176px;font-size:9px;letter-spacing:3px;color:var(--ink)}
.cover .artist{position:absolute;left:58px;top:186px;font-family:'Great Vibes',cursive;font-size:48px;color:var(--gold)}
.cover .day{position:absolute;left:60px;top:288px;width:92px;text-align:center;font-size:15px;font-weight:500;border:1px solid var(--ink);padding:2px 0}
.cover .date{position:absolute;left:60px;top:310px;font-size:48px;font-weight:400;color:var(--ink);line-height:1.1}
.cover .date sup{font-size:28px;vertical-align:top;position:relative;top:6px}
.cover .month{position:absolute;left:60px;top:370px;width:92px;text-align:center;font-size:16px;font-weight:600;background:var(--gold);color:var(--teal-deep)}
.cover .time{position:absolute;left:60px;top:392px;font-size:14px;font-weight:600;color:var(--ink)}
.cover .photo{position:absolute;left:210px;top:190px;width:245px;height:440px;
  background:linear-gradient(160deg,#2a2a2a 0%,#3f6f66 45%,#1e4a40 70%,#0d1f1f 100%)}
.cover .ornament-top{position:absolute;right:-30px;top:-30px;width:150px;height:150px;border-radius:50%;
  background:radial-gradient(circle,rgba(201,146,74,.35),rgba(201,146,74,0) 70%)}
.cover .notes{position:absolute;left:250px;top:100px;width:140px;height:100px;
  background:linear-gradient(135deg,rgba(232,194,122,0),rgba(232,194,122,.28),rgba(232,194,122,0))}
.cover .banner{position:absolute;left:24px;right:24px;bottom:38px;height:68px;border:2px solid var(--gold);background:#0c3432}
.cover .banner-photo{position:absolute;top:6px;width:48px;height:44px;background:linear-gradient(150deg,#6b5a4a,#2d2520)}
.cover .banner-photo.left{left:10px}
.cover .banner-photo.right{right:10px}
.cover .banner-name{position:absolute;left:0;right:0;top:14px;text-align:center;font-family:'Cinzel',serif;font-size:26px;color:var(--gold)}
.cover .banner-credit{position:absolute;bottom:3px;font-size:6px;letter-spacing:1px;color:var(--ink-soft)}
.cover .banner-credit.left{left:10px}
.cover .banner-credit.right{right:10px}
</style>
</head>
<body>

<!-- Cover -->
<section class="page cover" style="left:104px;top:189px">
  <div class="ornament-top" role="img" aria-label="Gold mandala ornament"></div>
  <div class="notes" role="img" aria-label="Gold musical staff with flowing notes"></div>
  <div class="photo" role="img" aria-label="Photo of the young pianist seated at a grand piano"></div>
  <div class="lotus lotus-left" role="img" aria-label="Teal lotus flower ornament"></div>
  <div class="lotus lotus-right" role="img" aria-label="Teal lotus flower ornament"></div>
  <div class="band-name">Band Foxglove</div>
  <div class="debut">DEBUT CONCERT</div>
  <div class="featuring">FEATURING</div>
  <div class="artist">Oveli</div>
  <div class="day">SATURDAY</div>
  <div class="date">12<sup>TH</sup></div>
  <div class="month">AUGUST</div>
  <div class="time">7:00–8:00PM</div>
  <div class="banner">
    <div class="banner-photo left" role="img" aria-label="Photo of the lead vocalist at the piano"></div>
    <div class="banner-photo right" role="img" aria-label="Photo of the guitarist"></div>
    <div class="banner-name">Band Foxglove</div>
    <div class="banner-credit left">OVELI – LEAD VOCAL &amp; PIANO</div>
    <div class="banner-credit right">TEVAN – GUITAR</div>
  </div>
</section>

<!-- Programme -->
<section class="page programme" style="left:621px;top:189px">
  <div class="frame"></div>
  <div class="lotus lotus-left" role="img" aria-label="Teal lotus flower ornament"></div>
  <div class="lotus lotus-right" role="img" aria-label="Teal lotus flower ornament"></div>
  <div class="content" style="top:66px">
    <div class="section"><h2 class="title">CLASSICAL</h2>
      <svg class="flourish" width="60" height="6"><path d="M2 3 Q15 0 30 3 Q45 6 58 3" stroke="#c9924a" fill="none"/></svg>
      <ul><li>Minuet in F Major</li><li>Moonlight Sonata</li><li>Climb Ev'ry Mountain</li></ul></div>
    <div class="section"><h2 class="title">BROADWAY</h2>
      <svg class="flourish" width="60" height="6"><path d="M2 3 Q15 0 30 3 Q45 6 58 3" stroke="#c9924a" fill="none"/></svg>
      <ul><li>Jingle Bells</li><li>Castle On A Cloud</li><li>My Favorite Things</li><li>Over the Rainbow</li></ul></div>
    <div class="section"><h2 class="title">ROCK</h2>
      <svg class="flourish" width="60" height="6"><path d="M2 3 Q15 0 30 3 Q45 6 58 3" stroke="#c9924a" fill="none"/></svg>
      <ul><li>Sacrifice</li><li>Your Song</li><li>Piano Man</li><li>My Way</li></ul></div>
    <div class="section"><h2 class="title">OVELI'S OWN COMPOSITIONS</h2>
      <svg class="flourish" width="60" height="6"><path d="M2 3 Q15 0 30 3 Q45 6 58 3" stroke="#c9924a" fill="none"/></svg>
      <ul><li>Pony's In Denver</li><li>Sunshine Up High</li><li>Gems and Jewels</li><li>Feel the Light</li></ul></div>
  </div>
</section>

<!-- Jingle Bells -->
<section class="page" style="left:104px;top:966px">
  <div class="frame"></div>
  <div class="lotus lotus-left" role="img" aria-label="Teal lotus flower ornament"></div>
  <div class="lotus lotus-right" role="img" aria-label="Teal lotus flower ornament"></div>
  <div class="content">
    <h2 class="title">JINGLE BELLS</h2>
    <svg class="flourish" width="60" height="6"><path d="M2 3 Q15 0 30 3 Q45 6 58 3" stroke="#c9924a" fill="none"/></svg>
    <p class="intro">"Jingle Bells" is one of the best-known and most widely sung songs in the world. It was first published in the middle of the nineteenth century and was once sung for a harvest holiday gathering. Although it has no original link to Christmas, it became tied to winter and to the Christmas season in the decades that followed.</p>
    <div class="lyrics">
      <p>Dashing through the snow<br>In a one-horse open sleigh<br>O'er the fields we go<br>Laughing all the way<br>Bells on bobtails ring<br>Making spirits bright<br>What fun it is to ride and sing<br>A sleighing song tonight, oh!</p>
      <p>Jingle bells, jingle bells<br>Jingle all the way<br>Oh, what fun it is to ride<br>In a one-horse open sleigh, hey!<br>Jingle bells, jingle bells<br>Jingle all the way<br>Oh what fun it is to ride<br>In a one-horse open sleigh</p>
      <p>Now the ground is white<br>Go it while you're young<br>Take the girls tonight<br>Sing this sleighing song<br>Just get a bobtailed bay<br>Two forty for his speed<br>And hitch him to an open sleigh<br>And you will take the lead</p>
    </div>
    <svg class="icon" width="40" height="34" viewBox="0 0 40 34"><path d="M10 6 Q20 8 18 22 L4 26 Q8 18 10 6Z M30 6 Q20 8 22 22 L36 26 Q32 18 30 6Z" fill="#d4a55a"/><circle cx="12" cy="28" r="3" fill="#d4a55a"/><circle cx="28" cy="28" r="3" fill="#d4a55a"/></svg>
  </div>
</section>

<!-- Over the Rainbow -->
<section class="page" style="left:621px;top:966px">
  <div class="frame"></div>
  <div class="lotus lotus-left" role="img" aria-label="Teal lotus flower ornament"></div>
  <div class="lotus lotus-right" role="img" aria-label="Teal lotus flower ornament"></div>
  <div class="content">
    <h2 class="title">OVER THE RAINBOW</h2>
    <svg class="flourish" width="60" height="6"><path d="M2 3 Q15 0 30 3 Q45 6 58 3" stroke="#c9924a" fill="none"/></svg>
    <p class="intro">"Over the Rainbow" is a ballad written for a classic musical film of the late 1930s. It was sung by the young star in her leading role and became her signature song. It won the top film award for best original song. The song is about hope: that the bad times will one day be over, and that a brighter place waits somewhere beyond.</p>
    <div class="lyrics">
      <p>When the sky above is grey and low<br>And the quiet rain begins to fall,<br>I look for colours in the glow.</p>
      <p>When the evening clouds grow dark and wide<br>There's a bright road leading far away,<br>It calls me from the other side,<br>To a softer place to stay,<br>Just a step beyond the grey.</p>
      <p>Somewhere past the hills, a light shines through,<br>There's a land I dreamed of long ago.<br>Somewhere past the hills the sky is blue,<br>And the hopes we hold will grow.</p>
      <p>One day I'll wake and find the storm has gone behind me,<br>Where worries melt like snow and fade from view.<br>That's where you'll find me.<br>Somewhere past the hills the songbirds fly,<br>They take their wings, so why, oh why can't I?</p>
    </div>
    <svg class="icon" width="60" height="34" viewBox="0 0 60 34"><g fill="none" stroke="#d4a55a" stroke-width="3"><path d="M8 30 A22 22 0 0 1 52 30"/><path d="M14 30 A16 16 0 0 1 46 30"/><path d="M20 30 A10 10 0 0 1 40 30"/></g><ellipse cx="10" cy="30" rx="9" ry="4" fill="#d4a55a"/><ellipse cx="50" cy="30" rx="9" ry="4" fill="#d4a55a"/></svg>
  </div>
</section>

<!-- Minuet / Moonlight -->
<section class="page" style="left:104px;top:1744px">
  <div class="frame"></div>
  <div class="lotus lotus-left" role="img" aria-label="Teal lotus flower ornament"></div>
  <div class="lotus lotus-right" role="img" aria-label="Teal lotus flower ornament"></div>
  <div class="content">
    <h2 class="title">MENUET IN F MAJOR</h2>
    <svg class="flourish" width="60" height="6"><path d="M2 3 Q15 0 30 3 Q45 6 58 3" stroke="#c9924a" fill="none"/></svg>
    <p class="intro">This composer is without doubt one of the greatest of all time, and one of the best known in the classical era. He was born into a musical family; his father was a violinist, teacher and composer who toured the courts of Europe with his gifted children.<br><br>Written for piano when the composer was a small child, this Minuet in F Major has a simple two-part texture. The right hand plays the melody while the left hand supplies the bass that holds it up.</p>
    <h2 class="title" style="margin-top:22px">MOONLIGHT SONATA</h2>
    <svg class="flourish" width="60" height="6"><path d="M2 3 Q15 0 30 3 Q45 6 58 3" stroke="#c9924a" fill="none"/></svg>
    <p class="intro">The Moonlight Sonata, a solo piano work, is admired for its gentle, flowing first movement. The piece was completed in 1801 and dedicated to a young student of the composer. Its popular name came years later, when a critic compared the music to moonlight shining on a quiet lake at night.<br><br>The sonata was bold in shape for its time. Most sonatas of the era opened with a lively movement, yet this one begins slowly and softly, then builds to a stormy finale. The last movement is so fierce that pianists of the day were said to break strings, and the composer played with a heavy touch as his hearing faded.</p>
    <svg class="icon" width="50" height="34" viewBox="0 0 50 34"><path d="M28 4 A14 14 0 1 0 40 24 A11 11 0 1 1 28 4Z" fill="#d4a55a"/><ellipse cx="18" cy="30" rx="14" ry="4" fill="#d4a55a" opacity=".8"/></svg>
  </div>
</section>

<!-- Climb Ev'ry Mountain -->
<section class="page" style="left:621px;top:1744px">
  <div class="frame"></div>
  <div class="lotus lotus-left" role="img" aria-label="Teal lotus flower ornament"></div>
  <div class="lotus lotus-right" role="img" aria-label="Teal lotus flower ornament"></div>
  <div class="content">
    <h2 class="title">CLIMB EV'RY MOUNTAIN</h2>
    <svg class="flourish" width="60" height="6"><path d="M2 3 Q15 0 30 3 Q45 6 58 3" stroke="#c9924a" fill="none"/></svg>
    <p class="intro">"Climb Ev'ry Mountain" is a song from a much-loved 1959 stage musical and the film made from it six years later. It is sung as an anthem of courage, urging people to take every step toward reaching their dreams.</p>
    <div class="lyrics" style="font-size:8.6px">
      <p>Look past every hill,<br>Keep walking on,<br>Follow every trail,<br>Every path you know.</p>
      <p>Look past every hill,<br>Cross every stream,<br>Follow every light,<br>Till you find your dream.</p>
      <p>A dream worth holding on<br>Takes all the heart you hold,<br>Every day of your life<br>For as long as you live.</p>
      <p>Look past every hill,<br>Cross every stream,<br>Follow every light,<br>Till you find your dream.</p>
    </div>
    <svg class="icon" width="60" height="30" viewBox="0 0 60 30"><path d="M2 28 L20 6 L28 16 L36 4 L58 28Z" fill="#d4a55a"/><path d="M20 6 L16 12 L24 12Z M36 4 L31 11 L41 11Z" fill="#f3e0b0"/></svg>
  </div>
</section>

<!-- My Favorite Things -->
<section class="page" style="left:104px;top:2522px">
  <div class="frame"></div>
  <div class="lotus lotus-left" role="img" aria-label="Teal lotus flower ornament"></div>
  <div class="lotus lotus-right" role="img" aria-label="Teal lotus flower ornament"></div>
  <div class="content">
    <h2 class="title">MY FAVORITE THINGS</h2>
    <svg class="flourish" width="60" height="6"><path d="M2 3 Q15 0 30 3 Q45 6 58 3" stroke="#c9924a" fill="none"/></svg>
    <p class="intro">This song comes from the same 1959 stage musical and its later film. It is a song about chasing away fear by filling the mind with the things she loves when times are bad.</p>
    <div class="lyrics">
      <p>Raindrops on windows and warm cups of cocoa<br>Bright painted teapots and hats with a bow, oh<br>Brown paper parcels with ribbons and strings<br>These are a few of my favourite things</p>
      <p>Soft woollen blankets and fresh apple pastries<br>Bells in the morning and kites in the breeze<br>Swallows that glide as the evening bell rings<br>These are a few of my favourite things</p>
      <p>Girls in white dresses with bright satin sashes<br>Snowflakes that settle on noses and lashes<br>Silver-white winters that melt into springs<br>These are a few of my favourite things</p>
      <p>When the storm comes<br>When the thunder<br>When I'm feeling low<br>I simply remember the things that I love<br>And then it's not hard to go</p>
    </div>
    <svg class="icon" width="44" height="40" viewBox="0 0 44 40"><path d="M6 10 L22 6 L22 28" stroke="#d4a55a" stroke-width="2.5" fill="none"/><path d="M6 10 L6 32" stroke="#d4a55a" stroke-width="2.5"/><ellipse cx="4" cy="32" rx="4" ry="3" fill="#d4a55a"/><ellipse cx="20" cy="28" rx="4" ry="3" fill="#d4a55a"/><path d="M34 36 L34 6 Q40 10 34 16" stroke="#d4a55a" stroke-width="2.5" fill="none"/><ellipse cx="32" cy="36" rx="4" ry="3" fill="#d4a55a"/></svg>
  </div>
</section>

<!-- Castle on a Cloud -->
<section class="page" style="left:621px;top:2522px">
  <div class="frame"></div>
  <div class="lotus lotus-left" role="img" aria-label="Teal lotus flower ornament"></div>
  <div class="lotus lotus-right" role="img" aria-label="Teal lotus flower ornament"></div>
  <div class="content">
    <h2 class="title">CASTLE ON A CLOUD</h2>
    <svg class="flourish" width="60" height="6"><path d="M2 3 Q15 0 30 3 Q45 6 58 3" stroke="#c9924a" fill="none"/></svg>
    <p class="intro">A famous French novel of 1862 has been adapted into one of the longest-running musicals in the world, which opened in the West End in 1985. The story is set in early nineteenth-century France. "Castle on a Cloud" is sung in the first act of the musical. It is the audience's first meeting with the young girl, as she dreams of a better life where all children are loved and free.</p>
    <div class="lyrics">
      <p>There's a castle high above,<br>I like to go there when I dream.<br>No one there has floors to sweep,<br>Not in my castle in the sky.</p>
      <p>There's a room that's full of toys,<br>There are a hundred girls and boys,<br>No one shouts or makes me cry,<br>Not in my castle in the sky.</p>
      <p>There's a lady all in white,<br>She holds me close and sings goodnight,<br>She's kind to see and soft to touch,<br>She says "My dear, I love you so much."</p>
      <p>I know a place where no one's lost,<br>I know a place where no one's sad,<br>Tears are never there at all,<br>Not in my castle in the sky.</p>
    </div>
    <svg class="icon" width="64" height="28" viewBox="0 0 64 28"><path d="M6 26 Q0 26 2 20 Q4 14 12 16 Q14 6 24 8 Q30 0 40 6 Q50 4 52 14 Q62 14 62 22 Q62 26 56 26Z" fill="#d4a55a"/></svg>
  </div>
</section>

<!-- Sacrifice -->
<section class="page" style="left:360px;top:3291px">
  <div class="frame"></div>
  <div class="lotus lotus-left" role="img" aria-label="Teal lotus flower ornament"></div>
  <div class="lotus lotus-right" role="img" aria-label="Teal lotus flower ornament"></div>
  <div class="content">
    <h2 class="title">SACRIFICE</h2>
    <svg class="flourish" width="60" height="6"><path d="M2 3 Q15 0 30 3 Q45 6 58 3" stroke="#c9924a" fill="none"/></svg>
    <p class="intro">"Sacrifice" is a song by a celebrated English singer and pianist, written with his long-time lyricist and released on a 1989 album. The song tells how hard it is to stay faithful in a marriage when temptation is strong. After its success, the singer has played this song in many venues in the years since it was released.</p>
    <div class="lyrics">
      <p>It's a quiet sigh; when days grow long<br>When the old path fades; and the road feels wrong<br>Into the distance; of each passing year<br>Gentle hearts keep calling; and the way grows clear</p>
      <p>Cold, cold night; hard days for two<br>Some things get better, baby<br>Just passing through</p>
      <p>And it's no small thing; just a simple word<br>It's two hearts living; in two different worlds<br>But it's no small thing; no small thing<br>It's no small thing at all</p>
      <p>Quiet misunderstanding; after the fall<br>Patience builds a bridge; across the wall<br>We find direction; no one turned away<br>No need to wonder; when the sky turns grey</p>
      <p>Cold, cold night; hard days for two<br>Some things get better, baby<br>Just passing through</p>
      <p>And it's no small thing; just a simple word<br>It's two hearts living; in two different worlds<br>But it's no small thing; no small thing<br>It's no small thing at all</p>
    </div>
    <svg class="icon" width="64" height="40" viewBox="0 0 64 40"><path d="M2 38 Q32 18 62 38Z" fill="#d4a55a"/><path d="M30 4 h4 v6 h6 v4 h-6 v14 h-4 v-14 h-6 v-4 h6Z" fill="#d4a55a"/><path d="M14 14 h3 v4 h4 v3 h-4 v9 h-3 v-9 h-4 v-3 h4Z M47 14 h3 v4 h4 v3 h-4 v9 h-3 v-9 h-4 v-3 h4Z" fill="#d4a55a"/></svg>
  </div>
</section>

</body>
</html>
```